Baby Care Print Log for Nannies and Parents- Creating a brand/style I can use across different forms

I am creating a notebook for babysitters to use to communicate with parents about the children they care for. I will be creating many different forms (emergency contacts, daily logs, shopping lists, etc.)
I need a look and feel from which to style these forms from. I am starting by designing the daily baby care log. I need a designer to take my Word doc with just text on it, and create a visual approach to make this visually appealing.
I do not want this to be extremely "babyish" with cartoon styling. I want it to be more of a professional looking style. I would like to be able to color each different document a different color palette, yet keep the similar look and feel. My logo is attached for inspiration. I use real photography across my website velmorapath.com.
Updates
I will be re-designing my Wordpress website based on what design I like best and also will need other forms completed once I pick a design. I am hoping to work with someone who I can hire for further development needs as well. Added Saturday, February 11, 2017
Target Market(s)
Professional Parents
Industry/Entity Type
Education
Requirements
Must have
- color, pop, visual appeal
- Please use the color in my logo and any complementary colors that you think work well with it. I definitely like colored patterns, ombre, colored backgrounds, etc. I'd prefer for it not to be completely white with only pops of color here and there.
Nice to have
- My logo somewhere subtly on the form
- Photography elements
Should not have
- cartoon images of babies, etc. I use real photography across my website with the exception of my logo umbrella.

```html
<!DOCTYPE html>
<html lang="en">
<head>
<meta charset="utf-8">
<title>Velmora Notes – Daily Log</title>
<link rel="stylesheet" href="https://fonts.googleapis.com/css2?family=Open+Sans:wght@400;600;700&family=Gochi+Hand&display=swap">
<style>
  :root {
    --paper: #ffffff;
    --ink: #2d2d2d;
    --hand: #1f1f1f;
    --blue: #2f86c4;
    --pink: #e6417c;
    --pink-soft: #f5b3c8;
    --orange: #f27b4b;
    --coral: #ee5a45;
    --yellow: #f2b632;
    --yellow-line: #f6cf6e;
    --teal: #1f7f8b;
    --grass-dark: #4f7a2e;
    --grass-light: #9cc267;
  }
  * { box-sizing: border-box; margin: 0; padding: 0; }
  html, body { width: 897px; height: 1200px; overflow: hidden; background: var(--paper); }
  body { position: relative; font-family: "Open Sans", Arial, sans-serif; color: var(--ink); }

  .family-bar {
    position: absolute; left: 402px; top: 40px; width: 378px; height: 60px;
    background: var(--blue); color: #fff; font-size: 20px; letter-spacing: .5px;
    display: flex; align-items: center; justify-content: center;
  }
  .brand {
    position: absolute; left: 70px; top: 120px; height: 84px;
    display: flex; align-items: center; gap: 18px;
  }
  .brand-dot { width: 46px; height: 46px; border-radius: 50%; background: var(--blue); }
  .brand-name { font-size: 64px; font-weight: 600; color: var(--ink); letter-spacing: -1px; }

  .rule-double { position: absolute; left: 28px; width: 770px; }
  .rule-double::before, .rule-double::after {
    content: ""; position: absolute; left: 0; right: 0; height: 3px;
  }
  .rule-double::before { top: 0; background: var(--pink); }
  .rule-double::after { top: 8px; background: var(--pink-soft); height: 2px; }

  .hero {
    position: absolute; left: 14px; top: 228px; width: 794px; height: 326px;
    background: linear-gradient(180deg, var(--grass-light) 0%, #7ea94a 55%, var(--grass-dark) 85%, #6b5a48 100%);
  }
  .hero-strip { position: absolute; left: 14px; top: 554px; width: 794px; height: 4px; background: var(--pink); }

  .name-tag {
    position: absolute; left: 50px; top: 488px; width: 340px; height: 52px;
    background: #fff; border-radius: 8px; display: flex; align-items: center;
    font-family: "Gochi Hand", cursive; font-size: 28px; color: var(--hand);
  }
  .name-tag .child { flex: 1; padding-left: 30px; }
  .name-tag .date { border-left: 3px solid var(--orange); padding-left: 12px; width: 122px; height: 34px; line-height: 34px; }

  .card { position: absolute; background: #fff; border-radius: 14px; border: 4px solid; }
  .card-title { font-weight: 700; color: var(--blue); font-size: 17px; letter-spacing: .3px; }
  .hand { font-family: "Gochi Hand", cursive; color: var(--hand); }

  .activities { left: 444px; top: 246px; width: 336px; height: 424px; border-color: var(--coral); border-width: 6px; }
  .activities .card-title { text-align: center; margin-top: 26px; }
  .activities .hand { font-size: 31px; line-height: 43px; padding: 16px 20px 0 26px; }

  .naps { top: 592px; width: 172px; height: 266px; }
  .naps-sleep { left: 36px; border-color: var(--orange); }
  .naps-change { left: 216px; border-color: var(--yellow); }
  .naps .card-title { text-align: center; margin-top: 14px; }
  .log-grid { position: relative; display: grid; grid-template-columns: 1fr 1fr; margin-top: 14px; }
  .log-grid .col { padding: 0 8px; }
  .log-grid .col-head { font-size: 12px; color: var(--blue); text-decoration: underline; text-align: center; font-weight: 600; margin-bottom: 10px; }
  .log-grid .hand { font-size: 21px; line-height: 32px; white-space: nowrap; }
  .naps-sleep .divider { position: absolute; left: 50%; top: 28px; width: 2px; height: 170px; background: var(--orange); }
  .naps-change .divider { position: absolute; left: 50%; top: 28px; width: 2px; height: 170px; background: var(--blue); }
  .naps-sleep .spaced { line-height: 64px; }

  .mood {
    position: absolute; left: 36px; top: 872px; width: 352px; height: 68px;
    border: 4px solid var(--teal); border-radius: 12px; display: flex; align-items: center; padding-left: 18px;
  }
  .mood-label { color: var(--blue); font-weight: 700; font-size: 17px; margin-right: 6px; }
  .mood .hand { font-size: 28px; }

  .feeding { left: 436px; top: 700px; width: 366px; height: 254px; border-color: var(--orange); }
  .feeding .card-title { margin: 14px 0 0 16px; }
  .feed-table { width: 330px; margin: 6px 0 0 16px; border-collapse: collapse; }
  .feed-table th { font-size: 13px; font-weight: 400; color: var(--ink); text-align: left; padding-bottom: 2px; }
  .feed-table td { font-family: "Gochi Hand", cursive; font-size: 22px; height: 36px; border-bottom: 2px solid var(--yellow-line); vertical-align: bottom; color: var(--hand); }

  .footer-rule { position: absolute; left: 30px; top: 966px; width: 840px; height: 3px; background: var(--pink); }
  .note { position: absolute; top: 988px; }
  .note .card-title { font-size: 19px; }
  .note .hand { font-size: 33px; line-height: 42px; margin-top: 4px; }
  .note-special { left: 50px; width: 380px; }
  .note-groceries { left: 520px; width: 360px; }
  .note-divider { position: absolute; left: 480px; top: 996px; width: 2px; height: 44px; background: var(--pink); }
</style>
</head>
<body>
  <div class="family-bar">THE LINWOOD FAMILY</div>

  <div class="brand">
    <span class="brand-dot"></span>
    <span class="brand-name">Velmora Notes</span>
  </div>

  <div class="rule-double" style="top:214px"></div>

  <div class="hero" role="img" aria-label="Photograph of a child in red boots holding a rainbow umbrella on a grassy lawn"></div>
  <div class="hero-strip"></div>

  <div class="name-tag"><span class="child">MILO</span><span class="date">2/15/17</span></div>

  <section class="card activities">
    <h2 class="card-title">TODAY'S ACTIVITES</h2>
    <p class="hand">We had a great day! We saw Mrs. Alder at the park. We went for a long walk and ate lunch in the back yard. I'll see you early tomorrow at 7:30.</p>
  </section>

  <section class="card naps naps-sleep">
    <h2 class="card-title">NAPS</h2>
    <div class="log-grid">
      <span class="divider"></span>
      <div class="col"><div class="col-head">TIME</div><div class="hand spaced">10:00<br>1:30</div></div>
      <div class="col"><div class="col-head">LENGTH</div><div class="hand spaced">1 hour<br>2 hours</div></div>
    </div>
  </section>

  <section class="card naps naps-change">
    <h2 class="card-title">NAPS</h2>
    <div class="log-grid">
      <span class="divider"></span>
      <div class="col"><div class="col-head">WET</div><div class="hand">8:00am<br>10:00am<br>1:00pm<br>3:00pm</div></div>
      <div class="col"><div class="col-head">BM</div><div class="hand">&nbsp;<br>10:00am<br>&nbsp;<br>&nbsp;&nbsp;4:00pm</div></div>
    </div>
  </section>

  <div class="mood"><span class="mood-label">MOOD</span><span class="hand">Happy All Day :)</span></div>

  <section class="card feeding">
    <h2 class="card-title">FEEDING</h2>
    <table class="feed-table">
      <thead><tr><th>Time</th><th>Milk (Type)</th><th>Water</th><th>Food</th></tr></thead>
      <tbody>
        <tr><td>8:00</td><td>8oz</td><td></td><td></td></tr>
        <tr><td>10:00</td><td>8oz</td><td></td><td>Rice</td></tr>
        <tr><td>11:00</td><td></td><td>2oz</td><td></td></tr>
        <tr><td>1:00</td><td>8oz</td><td></td><td></td></tr>
        <tr><td>3:00</td><td>8oz</td><td></td><td></td></tr>
      </tbody>
    </table>
  </section>

  <div class="footer-rule"></div>

  <section class="note note-special">
    <h2 class="card-title">SPECIAL NOTES</h2>
    <p class="hand">I brought in the milk off the front porch.</p>
  </section>
  <div class="note-divider"></div>
  <section class="note note-groceries">
    <h2 class="card-title">GROCERIES</h2>
    <p class="hand">You are almost out of wipes.</p>
  </section>
</body>
</html>
```